quiet meadow therapy (QMT)

I need to build a website for my therapy business.
There are two parts to the website
on the landing page; they choose whether they are therapists making a referral or patients needing more information.
After that, they are taken to their respective pages.
There is the textual information and a referral form on the therapist page, and on the patient page, the text is a bit different, and there will be a booking page on the patient page.
Visually minimal, it's a therapeutic website. I want it clean, clinical, and modern
colors: greenish blue or maybe orangish
PHP/html code
Updates

Hi everyone
I'm very sorry for the lack of responses to your designs. I am trying to work it out, but this platform has been a challenge for me.
I appreciate everyone's efforts, and I am unsure how to rate designs and move forward with the ones I like. There is a 5-star rating, but I don't understand how I'm supposed to politely say that it is not it without feeling like I'm going to affect someone's future rating negatively.
Please understand me. Thank you

Designs look the same

Target Market(s)

therapy and stress management

Industry/Entity Type

stress management therapy

Coding

Coded - Design and coding required

Number of Pages Required

5+ page

Font styles to use
Serif

Colors
0094D4
00A9DD
6FCCEA
C7EBF8
E9F6FB
00AB8E
00BBA5
67D7C9
C6EFE9
E9F9F6

Requirements
Must have
• landing page that that have 2 options. one for therapist another for patient

```html
<!DOCTYPE html>
<html lang="en">
<head>
<meta charset="utf-8">
<title>Quiet Meadow Therapy</title>
<link rel="stylesheet" href="https://fonts.googleapis.com/css2?family=Oswald:wght@400;700&family=Open+Sans:ital,wght@0,400;0,700;1,400&family=Roboto:wght@400&family=PT+Serif&display=swap">
<style>
:root{
  --dark:#333333;
  --ink:#1f2329;
  --heading:#3a4350;
  --orange:#ff8000;
  --teal:#88c9b7;
  --slate:#878d98;
  --mist:#dfe3ea;
  --field:#575c66;
  --nav-active:#6fa1e0;
  --link:#5b95d8;
  --white:#ffffff;
}
*{box-sizing:border-box;margin:0;padding:0}
html,body{width:1200px;height:2973px;overflow:hidden}
body{position:relative;background:var(--white);font-family:"Open Sans",sans-serif;color:var(--ink)}
.abs{position:absolute}

.site-header{left:0;top:0;width:1200px;height:92px;background:var(--dark)}
.brand{display:flex;align-items:center;gap:12px}
.brand-mark{width:34px;height:34px;border-radius:50%;background:#5bbf9a}
.brand-name{font-family:"Open Sans",sans-serif;font-weight:400;font-size:38px;letter-spacing:14px;color:var(--white)}
.site-header .brand{left:110px;top:22px}
.main-nav{left:433px;top:32px;display:flex;font-family:"PT Serif",serif;font-size:13px;color:var(--white)}
.main-nav span{display:block;height:31px;line-height:31px;padding:0 17px}
.main-nav .active{background:var(--nav-active)}
.search{left:925px;top:30px;width:175px;height:32px;background:var(--white);border:1px solid #ccc;font-size:14px;color:#888;padding:6px 11px}
.search svg{position:absolute;right:9px;top:8px}

.hero{left:0;top:92px;width:1200px;height:785px;background:linear-gradient(100deg,#d4dde6 0%,#eef2f6 30%,#c9d3de 55%,#e4eaf0 80%,#bfcad6 100%)}
.hero-title{left:130px;top:370px;font-family:"Oswald",sans-serif;font-weight:700;font-size:52px;line-height:58px;color:var(--heading);text-transform:uppercase}
.hero-text{left:130px;top:553px;width:416px;font-size:14px;line-height:22.5px;text-align:justify;color:var(--ink)}
.btn-primary{left:130px;top:660px;width:133px;height:37px;background:var(--orange);color:var(--white);font-weight:700;font-size:12px;letter-spacing:1px;text-align:center;line-height:37px}

.choice{top:785px;width:501px;height:373px;color:var(--white);text-align:center}
.choice.therapist{left:99px;background:var(--teal)}
.choice.patient{left:600px;background:var(--slate)}
.choice-icon{position:absolute;left:204px;top:46px;width:93px;height:93px;border:2px solid var(--white);border-radius:50%;display:flex;align-items:center;justify-content:center}
.choice h2{position:absolute;left:0;width:100%;font-family:"Roboto",sans-serif;font-weight:400;font-size:20px}
.choice p{position:absolute;left:20px;width:461px;font-size:14px;line-height:22px}
.therapist h2{top:192px}.therapist p{top:233px}
.patient h2{top:211px}.patient p{top:252px}

.story-photo{left:99px;top:1203px;width:478px;height:340px;background:linear-gradient(120deg,#b8c8d6,#eef1f4 45%,#d9cfc2 75%,#c48a5c)}
.story-title{left:639px;top:1250px;font-family:"Oswald",sans-serif;font-weight:400;font-size:33px;line-height:35px;text-transform:uppercase;color:var(--ink)}
.story-text{left:639px;top:1337px;width:444px;font-size:14.5px;line-height:22.5px;text-align:justify}

.services{left:0;top:1588px;width:1200px;height:752px;background:var(--mist)}
.section-title{left:0;width:1200px;text-align:center;font-family:"Oswald",sans-serif;font-weight:400;font-size:34px;line-height:44px;text-transform:uppercase}
.section-lead{left:350px;width:500px;text-align:center;font-size:14.5px;line-height:22.5px}
.services .section-title{top:76px;color:var(--ink)}
.services .section-lead{top:132px}
.service{top:235px;width:322px;height:462px;background:var(--white)}
.service .photo{height:265px}
.service h3{position:absolute;left:18px;top:307px;font-family:"Roboto",sans-serif;font-weight:400;font-size:20px}
.service p{position:absolute;left:18px;top:349px;width:290px;font-size:12.5px;line-height:19.5px}
.service .more{position:absolute;left:18px;top:426px;font-weight:700;font-size:12px;letter-spacing:1px;color:var(--link)}

.contact{left:0;top:2340px;width:1200px;height:526px;background:var(--slate)}
.contact .section-title{top:66px;color:var(--white)}
.contact .section-lead{top:124px;color:var(--white)}
.field{left:277px;width:646px;background:var(--field);color:#c4c7cc;font-size:14px;padding:9px 10px}
.btn-submit{left:547px;top:435px;width:105px;height:36px;background:#e8eaee;font-weight:700;font-size:12px;letter-spacing:1px;text-align:center;line-height:36px;color:var(--ink)}

.site-footer{left:0;top:2866px;width:1200px;height:107px;background:var(--dark)}
.site-footer .brand{left:112px;top:30px}
.copyright{left:0;width:1200px;top:46px;text-align:center;font-style:italic;font-size:12.5px;color:var(--white)}
.social{left:993px;top:44px;display:flex;gap:11px}
.social span{width:18px;height:18px;border-radius:50%;background:#3b82d8}
</style>
</head>
<body>

<header class="site-header abs">
  <div class="brand abs"><span class="brand-mark"></span><span class="brand-name">QMT</span></div>
  <nav class="main-nav abs">
    <span class="active">HOME</span><span>ABOUT</span><span>THERAPIST</span><span>PATIENT</span><span>CONTACT</span>
  </nav>
  <div class="search abs">Search
    <svg width="14" height="14" viewBox="0 0 14 14"><circle cx="6" cy="6" r="4.5" fill="none" stroke="#999" stroke-width="1.4"/><line x1="9.3" y1="9.3" x2="13" y2="13" stroke="#999" stroke-width="1.4"/></svg>
  </div>
</header>

<section class="hero abs" role="img" aria-label="Smiling doctor in a white coat holding a clipboard in a bright clinic"></section>
<h1 class="hero-title abs">We help people<br>reach their full<br>potential</h1>
<p class="hero-text abs">Lorem ipsum dolor sit amet, consectetur adipisicing elit, sed do eiusmod tempor incididunt ut labore et dolore magna aliqua. Ut enim ad minim veniam, quis nostrud exercitation ullamco laboris nisi ut aliquip ex ea commodo consequat.</p>
<div class="btn-primary abs">READ MORE</div>

<div class="choice therapist abs">
  <div class="choice-icon">
    <svg width="46" height="52" viewBox="0 0 46 52" fill="none" stroke="#fff" stroke-width="2" stroke-linejoin="round">
      <rect x="5" y="6" width="36" height="44" rx="3"/>
      <rect x="15" y="2" width="16" height="8" rx="2"/>
      <line x1="12" y1="20" x2="34" y2="20"/><line x1="12" y1="28" x2="34" y2="28"/><line x1="12" y1="36" x2="26" y2="36"/>
    </svg>
  </div>
  <h2>THERAPISTS MAKING A REFERRAL</h2>
  <p>Lorem ipsum dolor sit amet, consectetur adipiscing elit nullam nunc justo sagittis suscipit ultrices.</p>
</div>
<div class="choice patient abs">
  <div class="choice-icon">
    <svg width="52" height="46" viewBox="0 0 52 46" fill="none" stroke="#fff" stroke-width="2" stroke-linejoin="round">
      <rect x="4" y="14" width="44" height="28" rx="2"/>
      <line x1="2" y1="14" x2="50" y2="14"/>
      <line x1="26" y1="21" x2="26" y2="35"/><line x1="19" y1="28" x2="33" y2="28"/>
      <rect x="18" y="3" width="16" height="11" rx="2"/>
    </svg>
  </div>
  <h2>PATIENTS NEEDING MORE INFORMATION</h2>
  <p>Lorem ipsum dolor sit amet, consectetur adipiscing elit nullam nunc justo sagittis suscipit ultrices.</p>
</div>

<div class="story-photo abs" role="img" aria-label="Stressed woman resting her head on her hand at a desk"></div>
<h2 class="story-title abs">Tell your story change our<br>world</h2>
<p class="story-text abs">Lorem ipsum dolor sit amet, consectetur adipisicing elit, sed do eiusmod tempor incididunt ut labore et dolore magna aliqua. Ut enim ad minim veniam, quis nostrud exercitation ullamco laboris nisi ut aliquip ex ea commodo consequat. Duis aute irure dolor in reprehenderit in voluptate velit esse cillum dolore eu fugiat nulla pariatur. Excepteur sint occaecat cupidatat non proident, sunt in culpa qui officia deserunt mollit anim id est laborum.</p>

<section class="services abs">
  <h2 class="section-title abs">Our theraphy services</h2>
  <p class="section-lead abs">Lorem ipsum dolor sit amet, consectetur adipiscing elit nullam nunc justo sagittis suscipit ultrices.</p>
  <article class="service abs" style="left:99px">
    <div class="photo" role="img" aria-label="Young woman with long hair sitting outdoors" style="background:linear-gradient(135deg,#8e9398,#c7c9cb 50%,#6f6a66)"></div>
    <h3>INDIVIDUALS THERAPHY</h3>
    <p>Lorem ipsum dolor sit amet, consectetur adipiscing elit nullam nunc justo sagittis suscipit ultrices.</p>
    <span class="more">READ MORE</span>
  </article>
  <article class="service abs" style="left:439px">
    <div class="photo" role="img" aria-label="Couple holding hands in a field at sunset" style="background:linear-gradient(180deg,#f5dcd0,#f0a35a 55%,#6b3a18)"></div>
    <h3>COUPLES THERAPHY</h3>
    <p>Lorem ipsum dolor sit amet, consectetur adipiscing elit nullam nunc justo sagittis suscipit ultrices.</p>
    <span class="more">READ MORE</span>
  </article>
  <article class="service abs" style="left:778px">
    <div class="photo" role="img" aria-label="Mother with two small children outdoors in autumn" style="background:linear-gradient(135deg,#5a4a2a,#b07a3a 45%,#7b3a4a)"></div>
    <h3>FAMILIES THERAPHY</h3>
    <p>Lorem ipsum dolor sit amet, consectetur adipiscing elit nullam nunc justo sagittis suscipit ultrices.</p>
    <span class="more">READ MORE</span>
  </article>
</section>

<section class="contact abs">
  <h2 class="section-title abs">Get in touch</h2>
  <p class="section-lead abs">Lorem ipsum dolor sit amet, consectetur adipiscing elit nullam nunc justo sagittis suscipit ultrices.</p>
  <div class="field abs" style="top:194px;height:38px">Enter your Name</div>
  <div class="field abs" style="top:251px;height:38px">Enter a valid email address</div>
  <div class="field abs" style="top:309px;height:106px">Enter your message</div>
  <div class="btn-submit abs">SUBMIT</div>
</section>

<footer class="site-footer abs">
  <div class="brand abs"><span class="brand-mark"></span><span class="brand-name">QMT</span></div>
  <p class="copyright abs">Copyright © Quiet Meadow Therapy . All rights reserved 2022</p>
  <div class="social abs" aria-label="Social links"><span></span><span></span><span></span><span></span></div>
</footer>

</body>
</html>
```